Travel agency website refresh

I want to refresh and simplify my current Wordpress.com website. Same general color scheme but modernize and make it user friendly for all devices. Must work with Wordpress. No live booking engines. We are a boutique luxury travel agency. Think luxury, vacation, boho chic, elegant, lush, tropical, cruises, first class. Romance and adventure.
Updates

Target Market(s)

Luxury travelers

Industry/Entity Type

Travel

Coding

Coded - Design and coding required

Number of Pages Required

5+ page

Font styles to use
Sans Serif

Colors
0094D4
00A9DD
6FCCEA
C7EBF8
E9F6FB

Requirements
Must have
• Compatible with Wordpress.com, homepage, about page, contact page, faq page
Nice to have
• The homepage should quickly tell the consumer the type of travel I specialize in. My current website has this (journeyswithmaren.example). I’d like to incorporate the about me as a preview on the home page.
Should not have
• Harsh colors, look generic

```html
<!DOCTYPE html>
<html lang="en">
<head>
<meta charset="utf-8">
<title>Journeys with Maren</title>
<link rel="stylesheet" href="https://fonts.googleapis.com/css2?family=Montserrat:wght@400;500;600;700&family=Lilita+One&display=swap">
<style>
:root{
  --teal:#5cc0c4;
  --teal-dark:#3fa9ae;
  --teal-soft:#d4eef0;
  --teal-pale:#e9f6f7;
  --ink:#1c1c1e;
  --text:#2a2a2a;
  --white:#ffffff;
  --mist:#f4f6f8;
  --night:#1b1b1d;
}
*{margin:0;padding:0;box-sizing:border-box}
html,body{width:1200px;height:4044px;overflow:hidden}
body{position:relative;background:var(--white);font-family:'Montserrat',sans-serif;color:var(--text)}
.abs{position:absolute}

/* nav */
.site-nav{position:absolute;left:0;top:0;width:1200px;height:86px;background:var(--white);z-index:5;box-shadow:0 1px 0 rgba(0,0,0,.06)}
.nav-link{position:absolute;top:36px;font-size:15px;font-weight:600;color:var(--ink);letter-spacing:.3px}
.nav-link.is-active{color:var(--teal)}
.nav-cta{position:absolute;right:0;top:0;width:198px;height:86px;background:var(--teal);color:var(--white);font-size:15px;font-weight:600;display:flex;align-items:center;justify-content:center}
.brand-badge{position:absolute;left:521px;top:6px;width:158px;height:158px;border-radius:50%;background:var(--white);z-index:6;display:flex;align-items:center;justify-content:center;text-align:center;box-shadow:0 2px 6px rgba(0,0,0,.08)}
.brand-name{font-size:15px;font-weight:700;color:var(--ink);line-height:1.25;letter-spacing:.5px}

/* hero */
.hero{position:absolute;left:0;top:86px;width:1200px;height:614px;background:linear-gradient(180deg,#c9d3db 0%,#aab8c1 30%,#5d6a5f 55%,#e6ecf0 80%,#ffffff 100%)}
.hero-title{position:absolute;font-family:'Lilita One',sans-serif;font-size:58px;color:var(--white);-webkit-text-stroke:2px var(--ink);letter-spacing:2px;line-height:1;white-space:nowrap}
.watch{position:absolute;left:984px;top:382px;font-size:13px;font-weight:700;color:var(--white);line-height:21px}
.play{position:absolute;left:1084px;top:372px;width:56px;height:56px;border-radius:50%;background:var(--teal);display:flex;align-items:center;justify-content:center}
.play-line{position:absolute;left:1140px;top:399px;width:60px;height:2px;background:var(--ink)}

/* shared */
.section-title{position:absolute;font-size:28px;font-weight:600;color:var(--ink);letter-spacing:.5px;white-space:nowrap}
.dot{position:absolute;width:28px;height:28px;border-radius:50%;background:var(--teal-soft);border:2px solid var(--teal)}
.body-copy{position:absolute;font-size:15px;line-height:38.5px;color:var(--text)}
.btn{position:absolute;width:191px;height:59px;border:2px solid var(--teal);border-bottom-width:5px;background:var(--white);color:var(--ink);font-size:18px;font-weight:600;display:flex;align-items:center;justify-content:center}

/* about */
.blob-back{position:absolute;border-radius:50%;background:var(--teal-pale)}
.photo{position:absolute}
.balloon-deco{position:absolute;left:1050px;top:1100px;width:230px;height:300px;border-radius:50%;background:var(--teal-pale);opacity:.8}

/* specialization */
.spec-band{position:absolute;left:0;top:1316px;width:1200px;height:760px;background:var(--mist)}
.tile{position:absolute;overflow:hidden}
.tile-label{position:absolute;left:20px;bottom:20px;font-size:23px;font-weight:600;color:var(--white);letter-spacing:.3px;white-space:nowrap}
.btn-light{background:#eef1f4}

/* testimonials */
.quote-band{position:absolute;left:192px;top:2848px;width:1008px;height:159px;background:linear-gradient(90deg,#5cc0c4,#6ccbcd)}
.testimonial-photo{position:absolute;left:880px;top:2640px;width:320px;height:367px;background:linear-gradient(180deg,#f2f4f5 0%,#d6d9db 45%,#9d958b 75%,#6b635a 100%)}
.client{position:absolute;left:243px;top:2893px;font-size:22px;font-weight:600;color:var(--white)}

/* footer */
.footer{position:absolute;left:0;top:3652px;width:1200px;height:392px;background:var(--night)}
.foot-head{position:absolute;font-size:19px;font-weight:500;color:var(--teal)}
.foot-link{position:absolute;font-size:15px;font-weight:500;color:var(--white)}
.news-input{position:absolute;left:831px;top:3806px;width:198px;height:55px;background:var(--white);font-size:12px;font-weight:500;color:var(--ink);padding:20px 13px}
.news-btn{position:absolute;left:1029px;top:3806px;width:60px;height:55px;background:var(--teal);display:flex;align-items:center;justify-content:center}
.foot-rule{position:absolute;left:110px;top:3975px;width:980px;height:1px;background:#3a3a3c}
.copyright{position:absolute;left:0;top:4004px;width:1200px;text-align:center;font-size:13px;font-weight:500;color:var(--white);word-spacing:2px}
</style>
</head>
<body>

<header class="site-nav">
  <span class="nav-link is-active" style="left:113px">HOME</span>
  <span class="nav-link" style="left:239px">ABOUT ME</span>
  <span class="nav-link" style="left:402px">BLOG</span>
  <span class="nav-link" style="left:721px">LET'S CONNECT</span>
  <span class="nav-link" style="left:922px">FAQS</span>
  <span class="nav-cta">CONTACT US</span>
</header>
<div class="brand-badge"><span class="brand-name">JOURNEYS<br>WITH MAREN</span></div>

<section class="hero" role="img" aria-label="Two travellers running and leaping through deep snow in front of a forested mountain valley"></section>
<div class="hero-title" style="left:85px;top:211px">JOURNEYS WITH</div>
<div class="hero-title" style="left:285px;top:298px">MAREN</div>
<div class="watch">WATCH OUR<br>VIDEO</div>
<div class="play"><svg width="20" height="22" viewBox="0 0 20 22"><path d="M3 2 L18 11 L3 20 Z" fill="#fff"/></svg></div>
<div class="play-line"></div>

<!-- about -->
<div class="blob-back" style="left:118px;top:755px;width:440px;height:440px"></div>
<div class="photo" role="img" aria-label="Couple with backpacks seated on rocks, pointing across a turquoise mountain lake" style="left:100px;top:780px;width:480px;height:440px;border-radius:50%;background:linear-gradient(180deg,#dfe7ee 0%,#6a8c8f 30%,#2f8f9c 55%,#3c6f7a 75%,#9a9289 100%)"></div>
<div class="balloon-deco"></div>
<span class="dot" style="left:663px;top:785px"></span>
<h2 class="section-title" style="left:720px;top:783px">ABOUT ME</h2>
<p class="body-copy" style="left:661px;top:842px;width:450px">Travel's in my blood! Growing up, my family owned a travel agency and, before I even knew I wanted to be a travel agent, I was off seeing the world—and gaining an appreciation for a well-planned trip. After graduating Northbridge College of Travel Studies in 1996, I've held management positions with several internationally acclaimed travel companies.</p>
<span class="btn" style="left:661px;top:1140px">LEARN MORE</span>

<!-- specialization -->
<div class="spec-band"></div>
<span class="dot" style="left:421px;top:1390px"></span>
<h2 class="section-title" style="left:474px;top:1388px">OUR SPECIALIZATION</h2>
<div class="tile" role="img" aria-label="Family playing with a kite on a sunny turquoise beach" style="left:110px;top:1486px;width:649px;height:263px;background:linear-gradient(180deg,#a8c8d8 0%,#3fb5be 45%,#8fb8b6 75%,#7d7468 100%)"><span class="tile-label">FAMILY VACATIONS</span></div>
<div class="tile" role="img" aria-label="Honeymoon couple walking hand in hand along a white tropical beach" style="left:773px;top:1486px;width:317px;height:541px;background:linear-gradient(180deg,#2b4fa8 0%,#6d8fd0 35%,#3fc0c9 55%,#e6eef0 75%,#b0aaa2 100%)"><span class="tile-label" style="left:10px;font-size:21px">HONEYMOON &amp; ROMANCE</span></div>
<div class="tile" role="img" aria-label="Palm tree over a turquoise lagoon and white sand" style="left:110px;top:1763px;width:319px;height:264px;background:linear-gradient(180deg,#3d6d3a 0%,#2fa5b0 45%,#d9dfd6 70%,#6e6e6a 100%)"><span class="tile-label">CUSTOM TRAVEL</span></div>
<div class="tile" role="img" aria-label="Cruise ship sailing at sunset" style="left:441px;top:1763px;width:318px;height:264px;background:linear-gradient(180deg,#c98b62 0%,#d7b39a 35%,#6f7683 60%,#333a45 100%)"><span class="tile-label">CRUISING</span></div>

<div class="photo" role="img" aria-label="Hiker in a yellow jacket looking out over a grassy valley toward snowy mountains" style="left:0;top:2040px;width:1200px;height:410px;background:linear-gradient(180deg,#f4f6f8 0%,#c9d2da 28%,#6f7f8f 45%,#6d7a4a 65%,#4e5a2e 100%);clip-path:polygon(0 0,100% 0,100% 94%,94% 97%,88% 93%,80% 98%,72% 94%,64% 99%,56% 95%,48% 98%,40% 93%,32% 99%,24% 95%,16% 98%,8% 94%,0 98%)"></div>
<span class="btn btn-light" style="left:504px;top:2078px">VIEW MORE</span>

<!-- testimonials -->
<span class="dot" style="left:119px;top:2527px"></span>
<h2 class="section-title" style="left:173px;top:2525px">OUR TESTIMONIALS</h2>
<div class="abs" style="left:110px;top:2625px;width:107px;height:1px;background:var(--ink)"></div>
<p class="body-copy" style="left:243px;top:2604px;width:540px">Maren is a pleasure to work with and very helpful and informative. She made planning our first cruise an easy experience. I would highly recommend Maren and the services she offers if your looking for someone to plan your vacation and make the process and easy one. Thank you so much from my wife Helen and I.</p>
<div class="quote-band"></div>
<div class="testimonial-photo" role="img" aria-label="Backpacker standing on a rocky outcrop above the valley"></div>
<div class="abs" style="left:780px;top:2773px;width:1px;height:102px;background:var(--ink)"></div>
<span class="client">THOMAS K</span>
<svg class="abs" style="left:243px;top:2935px" width="90" height="22" viewBox="0 0 90 22"><path d="M32 11H2M2 11l8-7M2 11l8 7M58 11h30M88 11l-8-7M88 11l-8 7" stroke="#fff" stroke-width="2" fill="none"/></svg>
<svg class="abs" style="left:753px;top:2918px" width="54" height="40" viewBox="0 0 54 40"><path d="M4 40V22C4 10 10 3 22 0l2 5c-7 3-10 7-10 13h9v22zM31 40V22C31 10 37 3 49 0l2 5c-7 3-10 7-10 13h9v22z" fill="#fff"/></svg>

<!-- babymoons -->
<span class="dot" style="left:116px;top:3116px"></span>
<h2 class="section-title" style="left:173px;top:3115px">ZIKA FREE BABYMOONS</h2>
<p class="body-copy" style="left:115px;top:3173px;width:455px">A Babymoon celebrates that special, fleeting time in a couple's life before a new (and very demanding) addition is welcomed into the family. Savoring a bit of time together in a place with stunning scenery, scrumptious cuisine, and relaxing activities is an ideal antidote to pregnancy's sleepless nights, swollen ankles, and world of worries.</p>
<span class="btn" style="left:115px;top:3472px">READ MORE</span>
<div class="blob-back" style="left:648px;top:3110px;width:440px;height:440px"></div>
<div class="photo" role="img" aria-label="Expecting couple smiling together in an airplane cabin" style="left:610px;top:3110px;width:480px;height:440px;border-radius:50%;background:linear-gradient(135deg,#dfe3e6 0%,#b7bcc0 30%,#3b5f8a 55%,#49b8dc 80%,#e8f4f8 100%)"></div>

<!-- footer -->
<svg class="abs" style="left:0;top:3622px" width="1200" height="32" viewBox="0 0 1200 32" preserveAspectRatio="none"><path d="M0 32V18l40-6 30 8 50-10 40 6 60-8 30 10 70-9 50 5 60-7 40 8 70-10 50 7 60-6 40 9 70-10 50 6 60-7 40 8 70-9 50 6 60-8 40 9 60-7 40 5 30-8V32z" fill="#1b1b1d"/></svg>
<footer class="footer"></footer>
<div class="abs" style="left:100px;top:3805px;width:240px;text-align:center;font-size:26px;font-weight:700;color:var(--white);line-height:1.2">JOURNEYS<br>WITH MAREN</div>
<span class="foot-head" style="left:463px;top:3747px">QUICK LINKS</span>
<span class="foot-link" style="left:463px;top:3810px">HOME</span>
<span class="foot-link" style="left:463px;top:3859px">ABOUT ME</span>
<span class="foot-link" style="left:463px;top:3906px">BLOG</span>
<span class="foot-link" style="left:600px;top:3810px">LET'S CONNECT</span>
<span class="foot-link" style="left:600px;top:3859px">FAQS</span>
<span class="foot-head" style="left:829px;top:3747px">NEWSLETTER</span>
<div class="news-input">EMAIL ADDRESS</div>
<div class="news-btn"><svg width="20" height="20" viewBox="0 0 20 20"><path d="M2 9 18 2 12 18 9 11z" fill="none" stroke="#1b1b1d" stroke-width="2" stroke-linejoin="round"/></svg></div>
<div class="foot-rule"></div>
<div class="copyright">COPYRIGHT © 2024 &nbsp;&nbsp;&nbsp;&nbsp;&nbsp;&nbsp;&nbsp;&nbsp;|&nbsp;&nbsp;&nbsp;&nbsp;&nbsp;&nbsp;&nbsp;&nbsp; ALL RIGHTS RESERVED</div>

</body>
</html>
```